Harrowmere Fields Green Initiative Infographic

We need a flyer to distribute to new and existing tenants in our office park which explains our Green Initiatives. Harrowmere Fields Office Park is a Class A office park consisting of 5 commercial buildings and about 100 tenants. Some of our clients include Quillbyte, Vantorell and Dunmore Bask.

Please visit www.harrowmerefieldsofficepark.example for questions on our current "brand" and amenities. It is very important to follow the current “feel” we have on the website.

Here are the Green Initiatives we need to convey in this flyer:
1. All buildings Power Crest rated in 2009
2. Lighting and Energy Initiatives:
a.) Motion sensors added to all electrical and janitorial closest, storage areas and executive parking garages b.) Relamp from a 32W to a 28W bulb for all 2x4 fixtures in tenant offices and building common areas c.) Stairways relamped to 25W
d.) Relamped from T12 to T8 and LEDS in elevator cabs
e.) Relamped to LEDs in Elevators Lobby
f.) Relamped Restrooms to Compact Fluorescent

3. Plumbing: installed aerators on restroom faucets at .5 gallon per minute

4. Heating Ventilation Air Conditioning (HVAC) Energy Management System programming engineered for best performance. Secondly, all rooftop units have VFDs (Variable Frequency Drives) which controls fan speed for optimal efficiency.

5. Irrigation Systems all have rain sensors

6. Comprehensive recycling program includes the recycling of plastic, glass, cans, all types of paper, and cardboard. Secondly, construction recycling is required and captures about 70% for recycling

7. Implemented green contracts with janitorial, window cleaning, and pest control.

8. Sustainable purchasing procedures include items such as green cleaning products for janitorial and window cleaning

9. Annual Building Events such as a Page Trade where tenants donate used books in exchange for another book and the Transit Expo which partners with community partners: 781 Rideshare Services and the RVB Urban Rail Network.

10. 2013 earth day celebration will include a green fair, recycling awareness, education, commuting options, and several educational awareness events

Reason: Please submit designs as inforgraphics. Thank you.

• Must have:
"Harrowmere Fields Office Park" as prominent, same feel as website listed above, include all 10 initiaves,

```html
<!DOCTYPE html>
<html lang="en">
<head>
<meta charset="utf-8">
<title>Harrowmere Fields Office Park — Our Green Initiatives Projects</title>
<link rel="stylesheet" href="https://fonts.googleapis.com/css2?family=Bevan&family=Cabin+Condensed:wght@400;500&family=Cinzel:wght@400;500&display=swap">
<style>
  :root {
    --frame: #ffffff;
    --sky: #e9efdf;
    --sky-line: #dfe7d2;
    --field: #69a64a;
    --panel: #82b86c;
    --panel-edge: #8cbe77;
    --ribbon: #c9d6a3;
    --ribbon-shade: #b6c78c;
    --ink: #1f2a1b;
    --brand-ink: #3a3a3a;
    --num: #e4efd9;
    --title: #ffffff;
  }
  * { margin: 0; padding: 0; box-sizing: border-box; }
  html, body { width: 846px; height: 1200px; overflow: hidden; background: var(--frame); }
  .flyer {
    position: relative;
    width: 846px; height: 1200px;
    background: var(--frame);
    font-family: "Cabin Condensed", "Arial Narrow", sans-serif;
  }
  .sky {
    position: absolute; left: 12px; top: 12px; width: 822px; height: 364px;
    background: repeating-linear-gradient(90deg, var(--sky) 0 3px, var(--sky-line) 3px 4px);
  }
  .field {
    position: absolute; left: 12px; top: 376px; width: 822px; height: 812px;
    background: var(--field);
    border-top: 2px solid #f3f6ee;
  }
  .brand {
    position: absolute; left: 190px; top: 121px;
    display: flex; align-items: center; gap: 32px;
  }
  .brand-mark {
    width: 68px; height: 68px; border-radius: 50%;
    border: 4px solid var(--brand-ink);
  }
  .brand-name {
    font-family: "Cinzel", serif; color: var(--brand-ink);
    display: flex; flex-direction: column; align-items: flex-end;
  }
  .brand-name .primary { font-size: 30px; letter-spacing: 2px; line-height: 1; }
  .brand-name .secondary { font-size: 17px; letter-spacing: 3px; margin-top: 10px; line-height: 1; }
  .bulb {
    position: absolute; left: 719px; top: 12px; width: 48px; height: 150px;
    border-radius: 6px 6px 24px 24px;
    background: linear-gradient(90deg, #dcdcd6, #ffffff 45%, #d2d2cc);
  }
  .ribbon { position: absolute; left: 38px; top: 337px; width: 774px; height: 169px; }
  .ribbon-title {
    position: absolute; left: 38px; top: 337px; width: 774px; height: 169px;
    display: flex; flex-direction: column; justify-content: center; align-items: center;
    font-family: "Bevan", serif; font-size: 45px; line-height: 64px;
    color: var(--title); text-align: center;
    text-shadow: 1px 1px 0 #9aa67c, 2px 3px 4px rgba(60, 70, 40, .55);
  }
  .panel {
    position: absolute; top: 537px; width: 368px; height: 563px;
    background: var(--panel);
    border: 1px solid var(--panel-edge);
    box-shadow: 0 1px 3px rgba(40, 70, 30, .25);
    padding: 18px 14px 0 15px;
    color: var(--ink); font-size: 15.7px; line-height: 21.8px;
  }
  .panel-left { left: 42px; }
  .panel-right { left: 437px; text-align: justify; }
  .initiative { margin-bottom: 22px; }
  .initiative .num { color: var(--num); font-size: 13px; margin-right: 5px; }
  .panel-left .initiative { text-align: left; }
  .panel-left .justify { text-align: justify; }
</style>
</head>
<body>
<div class="flyer">
  <div class="sky"></div>
  <div class="field"></div>

  <div class="brand">
    <div class="brand-mark"></div>
    <div class="brand-name">
      <span class="primary">Harrowmere Fields</span>
      <span class="secondary">Office Park</span>
    </div>
  </div>

  <div class="bulb" role="img" aria-label="Compact fluorescent light bulb hanging from the top edge"></div>

  <svg class="ribbon" viewBox="0 0 774 169" aria-hidden="true">
    <polygon points="0,8 774,0 752,60 774,162 10,169 22,88" fill="var(--ribbon-shade)"/>
    <polygon points="4,0 770,0 748,58 770,158 6,160 26,80" fill="var(--ribbon)"/>
  </svg>
  <h1 class="ribbon-title"><span>OUR GREEN INITIATIVES</span><span>PROJECTS</span></h1>

  <section class="panel panel-left">
    <p class="initiative"><span class="num">1</span> All buildings Power Crest rated in 2009</p>
    <p class="initiative"><span class="num">2</span>Lighting and Energy Initiatives:<br>
      a.) Motion sensors added to all electrical and janitorial closest, storage areas and executive parking garages<br>
      b.) Relamp from a 32W to a 28W bulb for all 2x4 fixtures in tenant offices and building common areas<br>
      c.) Stairways relamped to 25W<br>
      d.) Relamped from T12 to T8 and LEDS in elevator cabs<br>
      e.) Relamped to LEDs in Elevators Lobby<br>
      f.) Relamped Restrooms to Compact Fluorescent</p>
    <p class="initiative justify"><span class="num">3</span>Plumbing: installed aerators on restroom faucets at .5 gallon per minute</p>
    <p class="initiative justify"><span class="num">4</span>Heating Ventilation Air Conditioning (HVAC) Energy Management System programming engineered for best performance. Secondly, all rooftop units have VFDs (Variable Frequency Drives) which controls fan speed for optimal efficiency.</p>
    <p class="initiative"><span class="num">5</span>Irrigation Systems all have rain sensors</p>
  </section>

  <section class="panel panel-right">
    <p class="initiative"><span class="num">6</span>Comprehensive recycling program includes the recycling of plastic, glass, cans, all types of paper, and cardboard. Secondly, construction recycling is required and captures about 70% for recycling</p>
    <p class="initiative"><span class="num">7</span>Implemented green contracts with janitorial, window cleaning, and pest control.</p>
    <p class="initiative"><span class="num">8</span>Sustainable purchasing procedures include items such as green cleaning products for janitorial and window cleaning</p>
    <p class="initiative"><span class="num">9</span>Annual Building Events such as a Page Trade where tenants donate used books in exchange for another book and the Transit Expo which partners with community partners: 781 Rideshare Services and the RVB Urban Rail Network.</p>
    <p class="initiative"><span class="num">10</span>2013 earth day celebration will include a green fair, recycling awareness, education, commuting options, and several educational awareness events</p>
  </section>
</div>
</body>
</html>
```